Small business services company needs a flyer designed

We need a flyer designed for a small building services company who has multiple roles ie- Roof, gutter and pressure cleaning, small building maintenance and garden cleanups. The company is based in Far North Queensland (Australia) where it is a tropical climate with lots of trees and green areas.

I want the colours to be based on the Logo and business card colours which will be added.

The flyer will need to be changeable so I can create monthly specials ie- Roof Cleaning Special, Gutter Cleaning Special or Pressure Cleaning special.

The roles of the business will be as stated on the attached business card.

Good evening all designers, please find below an update for you all, I hope it may answer some questions you have.

'd like the flyer to be DL size and at present I don't have any photo's. But i'd be happy for you to source some from google. The pictures I'd like would be of gutter cleaning from a ladder, pressure washing roofs & driveways with the large round "flat surface cleaners". Possibly have split pictures of the pressure cleaning to show before and after. 
Far North Queensland is a very tropical environment that has lots of palm trees and rain forest. The climate is usually 30+ degrees C. Incorporating those colours with the logo colours I'd like. 

Hello all designers.

I have just uploaded some of my own job pictures. There is a before and an after picture. If you source any other pictures, I'd like to see a flat surface/ spinmaster cleaner in operation, either on a roof or a driveway.

My goal is for a single sided flyer with all the details from my business card to be on the flyer. 

Please remember the climate in my area is very tropical and usually 30+ degrees C. Never cold or snowing. So please have pictures to reflect.

Thanks for the designs.
Regards,Darren

Reason: hi all designers. I have extended the deadline by 3 days to accommodate all the designers who have only recently accepted the brief nest invites. I have had a lot of declines and want the best designs I can choice from. This is no reflection of the calibre of the designs I have already received. I look forward to seeing all the updates and new designs. Regards, Darren

Home owners who take pride in the street appeal of their homes, or to add value to their selling price when a house goes on the sales market.

Building

```html
<!DOCTYPE html>
<html lang="en">
<head>
<meta charset="utf-8">
<title>Highline Roof, Gutter &amp; Pressure Cleaning – DL Flyer</title>
<link rel="stylesheet" href="https://fonts.googleapis.com/css2?family=Cinzel:wght@500;700&family=PT+Sans+Narrow:wght@700&family=Open+Sans:wght@400;600;700&display=swap">
<style>
  :root {
    --navy: #2b2f86;
    --royal: #2d3a96;
    --teal: #1fb3a2;
    --teal-dark: #159a8b;
    --paper: #ffffff;
    --stage: #eef3f5;
    --text-dark: #2a2d7c;
  }
  * { box-sizing: border-box; margin: 0; padding: 0; }
  html, body { width: 1104px; height: 1200px; overflow: hidden; background: var(--stage); }
  .flyer {
    position: absolute; left: 282px; top: 30px; width: 540px; height: 1140px;
    background: var(--paper); overflow: hidden;
    box-shadow: 0 6px 24px rgba(0,0,0,.18);
    font-family: "Open Sans", Arial, sans-serif;
  }
  .flyer-shapes { position: absolute; inset: 0; }
  .brand { position: absolute; left: 0; right: 0; text-align: center; color: var(--teal); font-family: "Cinzel", Georgia, serif; }
  .brand-top { top: 62px; }
  .brand-name { font-size: 50px; font-weight: 700; letter-spacing: 2px; line-height: 1; }
  .brand-tag { font-family: "Open Sans", Arial, sans-serif; font-size: 8.5px; font-weight: 700; color: var(--navy); letter-spacing: .6px; margin-top: 8px; }
  .call-line {
    position: absolute; top: 170px; left: 0; right: 0; text-align: center;
    font-family: "Cinzel", Georgia, serif; font-weight: 500; font-size: 29px; color: var(--teal); letter-spacing: 1px;
  }
  .snap { position: absolute; border: 4px solid #fff; box-shadow: 0 3px 8px rgba(0,0,0,.35); }
  .snap-gutter { left: 30px; top: 242px; width: 94px; height: 108px; transform: rotate(-3deg); background: linear-gradient(160deg,#dfe3e6,#8d9399 60%,#5b6166); }
  .snap-hose { left: 128px; top: 214px; width: 122px; height: 98px; transform: rotate(4deg); background: linear-gradient(170deg,#5d8a3a,#9bbf6a 55%,#c9c2b2); }
  .snap-roof { left: 258px; top: 240px; width: 118px; height: 112px; transform: rotate(-2deg); background: linear-gradient(180deg,#9fc3e4,#59616a 45%,#3c3d3f); }
  .snap-ladder { left: 380px; top: 218px; width: 130px; height: 112px; transform: rotate(3deg); background: linear-gradient(150deg,#4f7a3a,#8d8f8c 55%,#6a6c70); }
  .services {
    position: absolute; top: 378px; left: 0; right: 0; text-align: center;
    font-family: "PT Sans Narrow", "Arial Narrow", sans-serif; font-weight: 700;
    font-size: 23px; line-height: 33px; color: #fff;
  }
  .services .sectors { color: var(--teal); }
  .result { position: absolute; top: 553px; height: 302px; border: 4px solid #fff; box-shadow: 0 3px 10px rgba(0,0,0,.35); }
  .result-before { left: 28px; width: 238px; background: linear-gradient(180deg,#3f6b2e,#5a5a4e 40%,#2f2c28); }
  .result-after { left: 270px; width: 232px; background: linear-gradient(180deg,#4e7d38,#bfbcb2 40%,#d8d3c6); }
  .tag {
    position: absolute; top: 612px; padding: 5px 12px; color: #fff;
    font-family: "PT Sans Narrow", "Arial Narrow", sans-serif; font-weight: 700; font-size: 19px;
  }
  .tag-before { left: 30px; background: var(--navy); }
  .tag-after { left: 424px; background: var(--teal); }
  .contact { position: absolute; right: 42px; top: 882px; width: 270px; text-align: right; color: var(--text-dark); white-space: nowrap; }
  .contact-name { font-size: 19px; font-weight: 700; letter-spacing: 1.5px; }
  .contact-role { font-size: 11.5px; font-weight: 700; color: var(--teal); letter-spacing: 3px; margin-top: 1px; padding-bottom: 8px; border-bottom: 1px solid var(--navy); }
  .contact-company { font-family: "Cinzel", Georgia, serif; font-size: 19px; letter-spacing: 4px; margin-top: 20px; }
  .contact-services { font-size: 12px; font-weight: 700; color: var(--teal); margin-top: 2px; }
  .contact-lines { margin-top: 22px; font-size: 13px; font-weight: 600; line-height: 22px; }
  .contact-lines svg { width: 12px; height: 12px; vertical-align: -1px; margin-left: 4px; }
  .contact-lines .abn { color: var(--teal); font-weight: 700; }
  .brand-bottom { top: 1066px; left: 22px; right: auto; width: 170px; }
  .brand-bottom .brand-name { font-size: 23px; letter-spacing: 1px; }
  .brand-bottom .brand-tag { font-size: 5px; margin-top: 5px; letter-spacing: .2px; }
  .brand-bottom .brand-call { font-size: 8px; color: var(--navy); margin-top: 3px; letter-spacing: .5px; }
</style>
</head>
<body>
  <main class="flyer">
    <svg class="flyer-shapes" width="540" height="1140" viewBox="0 0 540 1140" aria-hidden="true">
      <polygon points="0,322 540,236 540,262 0,350" fill="var(--teal)"/>
      <polygon points="0,346 540,258 540,872 0,872" fill="var(--royal)"/>
      <polygon points="330,872 540,838 540,858 420,876" fill="var(--teal)"/>
      <path d="M235 872 C 195 960, 200 1080, 330 1136" fill="none" stroke="var(--navy)" stroke-width="5"/>
      <path d="M250 872 C 215 965, 220 1075, 345 1128" fill="none" stroke="var(--teal)" stroke-width="3"/>
    </svg>

    <header class="brand brand-top">
      <div class="brand-name">HIGHLINE</div>
      <div class="brand-tag">ROOF, GUTTER &amp; PRESSURE CLEANING SERVICES</div>
    </header>

    <p class="call-line">CALL DARREN 0400 555 214</p>

    <div class="snap snap-gutter" role="img" aria-label="Gloved hand clearing leaves from a roof gutter"></div>
    <div class="snap snap-hose" role="img" aria-label="Pressure washer cleaning a garden path"></div>
    <div class="snap snap-roof" role="img" aria-label="Worker pressure cleaning a tiled roof"></div>
    <div class="snap snap-ladder" role="img" aria-label="Tradesman repairing a roof gutter"></div>

    <section class="services">
      <p>Gutter Cleaning</p>
      <p>Pressure Cleaning - Roofs Driveways etc</p>
      <p>Minor Roof, Gutter &amp; Building Maintenance</p>
      <p>Garden waste Removal &amp; Complex Cleanups</p>
      <p class="sectors">Residential, Commercial &amp; Body Corporate Jobs</p>
    </section>

    <div class="result result-before" role="img" aria-label="Dirty outdoor staircase before pressure cleaning"></div>
    <div class="result result-after" role="img" aria-label="Clean outdoor staircase after pressure cleaning"></div>
    <span class="tag tag-before">Before</span>
    <span class="tag tag-after">After</span>

    <section class="contact">
      <p class="contact-name">DARREN KELLOW</p>
      <p class="contact-role">OWNER OPERATOR</p>
      <p class="contact-company">HIGHLINE</p>
      <p class="contact-services">Roof, Gutter &amp; Pressure Cleaning Services</p>
      <div class="contact-lines">
        <p>0400 555 214 :<svg viewBox="0 0 12 12"><path d="M3 1 L5 3.5 L4 5 Q5 7 7 8 L8.5 7 L11 9 L9.5 11 Q4 11 1 3 Z" fill="var(--navy)"/></svg></p>
        <p>roofcleaning@netmail.com.au :<svg viewBox="0 0 12 12"><rect x="1" y="2.5" width="10" height="7" fill="none" stroke="var(--navy)" stroke-width="1.2"/><path d="M1 2.5 L6 6.5 L11 2.5" fill="none" stroke="var(--navy)" stroke-width="1.2"/></svg></p>
        <p class="abn">ABN -12 345 678 901</p>
      </div>
    </section>

    <footer class="brand brand-bottom">
      <div class="brand-name">HIGHLINE</div>
      <div class="brand-tag">ROOF, GUTTER &amp; PRESSURE CLEANING SERVICES</div>
      <div class="brand-call">CALL DARREN 0400 555 214</div>
    </footer>
  </main>
</body>
</html>
```